Tulven Electrics Flyer Design Advertising

I am after an A5 Flyer design to help promote my electrical services business.
I would like to have information on what my business offers, photos of electrical work, and specials/deals for an amount of time.

Industry/Entity Type

Electrician

Font styles to use
Sans Serif

Colors
0292cd
33a6d7
85cae6
3176b5
333333
1b1b1b
ffffff
5c5c5c
474747

Requirements
Must have
• Specialising in New homes, renovations and commercial projects
• Contact details:
• ph. 0437 619 458
• email admin@tulvenelectrics.example.au
• facebook TulvenElectrics
• Specials/Deals:
• 10% off all electrical services
• or
• Free LED downlights on installation
• *Terms conditions apply
• ALL RESIDENTIAL & COMMERCIAL ELECTRICAL SERVICES
• - New Home installations
• - Commercial projects
• - Shop fit outs
• - Renovations
• - Smoke Detectors
• - Air Conditioning and Ceiling Fans
• - Garden Lighting
• - Oven and Cooktop Installations
• - Power Point installation
• - LED lighting upgrades
• - Security Lighting
• - Switchboard upgrades
• - Test and Tag
• - Commercial Property
• - General Electrical Maintenance

```html
<!DOCTYPE html>
<html lang="en">
<head>
<meta charset="utf-8">
<title>Tulven Electrics Flyer</title>
<link href="https://fonts.googleapis.com/css2?family=Roboto:ital,wght@0,400;0,500;0,700;0,900;1,900&family=Roboto+Condensed:wght@400;700&display=swap" rel="stylesheet">
<style>
  :root{
    --blue:#0292cd;
    --blue-mid:#33a6d7;
    --blue-pale:#85cae6;
    --blue-deep:#3176b5;
    --charcoal:#333333;
    --ink:#1b1b1b;
    --white:#ffffff;
    --grey:#5c5c5c;
    --grey-dark:#474747;
    --red:#e31e24;
    --backdrop:#e6e7e9;
  }
  *{margin:0;padding:0;box-sizing:border-box}
  html,body{width:1200px;height:1200px;overflow:hidden;background:var(--backdrop)}
  body{font-family:"Roboto",Arial,sans-serif;position:relative}
  .flyer{position:absolute;left:189px;top:14px;width:822px;height:1172px;background:var(--white);overflow:hidden;box-shadow:0 6px 24px rgba(0,0,0,.18)}
  .flyer__art{position:absolute;left:0;top:0;width:822px;height:1172px}
  .tagline{position:absolute;right:46px;top:30px;color:var(--white);font-size:12.5px;line-height:15px;text-align:right;font-weight:500}
  .brand{position:absolute;left:80px;top:41px;display:flex;align-items:center;gap:14px}
  .brand__dot{width:132px;height:132px;border-radius:50%;background:var(--blue);flex:none}
  .brand__name{font-weight:900;font-size:40px;color:var(--charcoal);letter-spacing:.5px;text-transform:uppercase;line-height:1}
  .services__title{position:absolute;left:41px;top:810px;font-family:"Roboto Condensed",Arial,sans-serif;font-weight:700;font-size:23.5px;color:var(--ink);letter-spacing:.1px}
  .services__list{position:absolute;top:855px;list-style:none;font-size:14px;color:var(--grey-dark);line-height:19.1px}
  .services__list--a{left:43px}
  .services__list--b{left:343px}
  .services__list li{padding-left:16px;position:relative}
  .services__list li::before{content:"✓";position:absolute;left:0;top:0;color:var(--blue-deep);font-weight:700;font-size:13px}
  .promo-burst__text{position:absolute;left:571px;top:860px;width:186px;text-align:center;color:var(--white);line-height:1}
  .promo-burst__free{font-size:40px;font-weight:900;font-style:italic;display:block}
  .promo-burst__led{font-size:27px;font-weight:700;display:block;margin-top:-2px}
  .promo-burst__rest{font-size:19px;display:block;line-height:26px;margin-top:3px}
  .contact{position:absolute;left:38px;top:1022px}
  .contact__row{display:flex;align-items:center;gap:8px;color:var(--ink)}
  .contact__row--phone{font-weight:700;font-size:41px;color:var(--blue-deep);line-height:48px}
  .contact__row--mail,.contact__row--social{font-family:"Roboto Condensed",Arial,sans-serif;font-size:20px;line-height:30px}
  .contact__row--social{font-size:23px}
  .contact__social-dot{width:26px;height:26px;border-radius:50%;border:2px solid var(--blue-deep);flex:none}
  .coupon{position:absolute;left:397px;top:1026px;width:368px;height:94px;border:2px dashed var(--ink)}
  .coupon__pct{position:absolute;left:14px;top:4px;font-family:"Roboto Condensed",Arial,sans-serif;font-weight:700;font-size:74px;line-height:82px;color:var(--red);letter-spacing:-3px}
  .coupon__off{position:absolute;left:138px;top:8px;font-family:"Roboto Condensed",Arial,sans-serif;font-weight:700;font-size:38px;line-height:40px;color:var(--red)}
  .coupon__what{position:absolute;left:210px;top:10px;font-family:"Roboto Condensed",Arial,sans-serif;font-size:15px;color:var(--ink)}
  .coupon__terms{position:absolute;left:205px;top:33px;font-family:"Roboto Condensed",Arial,sans-serif;font-size:12px;font-weight:700;color:var(--ink)}
  .coupon__expiry{position:absolute;left:154px;top:62px;font-family:"Roboto Condensed",Arial,sans-serif;font-size:15px;color:var(--ink);display:flex;align-items:center;gap:8px}
  .coupon__expiry-field{width:130px;height:20px;background:#b9b9b9}
  .footer-bar{position:absolute;left:0;bottom:0;width:822px;height:38px;background:var(--charcoal)}
</style>
</head>
<body>
<div class="flyer">
  <svg class="flyer__art" viewBox="0 0 822 1172" xmlns="http://www.w3.org/2000/svg">
    <defs>
      <linearGradient id="heroTone" x1="0" y1="0" x2="1" y2="1">
        <stop offset="0" stop-color="#5f8f4a"/>
        <stop offset=".35" stop-color="#e9eef0"/>
        <stop offset=".7" stop-color="#f4f1ea"/>
        <stop offset="1" stop-color="#cfd6cf"/>
      </linearGradient>
      <linearGradient id="midBlue" x1="0" y1="0" x2="1" y2="0">
        <stop offset="0" stop-color="var(--blue-mid)"/>
        <stop offset="1" stop-color="var(--blue)"/>
      </linearGradient>
      <linearGradient id="kitchenTone" x1="0" y1="0" x2="1" y2="1">
        <stop offset="0" stop-color="#c9d3d8"/><stop offset=".5" stop-color="#f2f2f2"/><stop offset="1" stop-color="#6a5a4c"/>
      </linearGradient>
      <linearGradient id="courtyardTone" x1="0" y1="0" x2="0" y2="1">
        <stop offset="0" stop-color="#4a5a2e"/><stop offset=".55" stop-color="#6b7a45"/><stop offset="1" stop-color="#1f4fb0"/>
      </linearGradient>
      <linearGradient id="poolTone" x1="0" y1="0" x2="0" y2="1">
        <stop offset="0" stop-color="#2c4a8c"/><stop offset=".5" stop-color="#5c5a60"/><stop offset="1" stop-color="#23a6c9"/>
      </linearGradient>
    </defs>
    <rect x="0" y="0" width="822" height="300" fill="var(--blue)"/>
    <rect x="0" y="430" width="822" height="300" fill="url(#midBlue)"/>
    <path d="M0,600 L822,580 L822,1172 L0,1172 Z" fill="var(--white)"/>
    <path d="M0,705 Q380,590 822,590 L822,1172 L0,1172 Z" fill="var(--white)"/>
    <path d="M0,705 Q380,590 822,590" fill="none" stroke="var(--charcoal)" stroke-width="9"/>
    <g role="img" aria-label="Photo of a bright open-plan living room with louvre windows and pool view">
      <path d="M0,10 Q380,12 822,142 L822,575 Q380,470 0,452 Z" fill="url(#heroTone)"/>
    </g>
    <path d="M0,10 Q380,12 822,142" fill="none" stroke="var(--charcoal)" stroke-width="12"/>
    <path d="M0,452 Q380,470 822,575" fill="none" stroke="var(--charcoal)" stroke-width="10"/>
    <g role="img" aria-label="Photo of a modern kitchen with pendant lights">
      <circle cx="156" cy="663" r="116" fill="url(#kitchenTone)"/>
    </g>
    <g role="img" aria-label="Photo of a lit courtyard garden beside a pool at night">
      <circle cx="407" cy="663" r="116" fill="url(#courtyardTone)"/>
    </g>
    <g role="img" aria-label="Photo of a two-storey house with lit pool at dusk">
      <circle cx="658" cy="663" r="116" fill="url(#poolTone)"/>
    </g>
    <polygon class="promo-burst-shape" fill="var(--red)" points="664,836 675,863 697,845 700,873 728,864 718,891 747,894 727,914 757,929 727,944 747,964 718,967 728,994 700,985 697,1013 675,995 664,1022 653,995 631,1013 628,985 600,994 610,967 581,964 601,944 571,929 601,914 581,894 610,891 600,864 628,873 631,845 653,863"/>
  </svg>

  <p class="tagline">Specialising in New homes,<br>renovations and commercial projects</p>

  <div class="brand">
    <span class="brand__dot"></span>
    <span class="brand__name">Tulven Electrics</span>
  </div>

  <h2 class="services__title">ALL RESIDENTIAL &amp; COMMERCIAL ELECTRICAL SERVICES</h2>
  <ul class="services__list services__list--a">
    <li>New Home installations</li>
    <li>Commercial projects</li>
    <li>Shop fit outs</li>
    <li>Renovations</li>
    <li>Smoke Detectors</li>
    <li>Air Conditioning and Ceiling Fans</li>
    <li>Garden Lighting</li>
    <li>Oven and Cooktop Installations</li>
  </ul>
  <ul class="services__list services__list--b">
    <li>Power Point installation</li>
    <li>LED lighting upgrades</li>
    <li>Security Lighting</li>
    <li>Switchboard upgrades</li>
    <li>Test and Tag</li>
    <li>Commercial Property</li>
    <li>General Electrical Maintenance</li>
  </ul>

  <div class="promo-burst__text">
    <span class="promo-burst__free">Free</span>
    <span class="promo-burst__led">LED</span>
    <span class="promo-burst__rest">downlights on<br>installation</span>
  </div>

  <div class="contact">
    <div class="contact__row contact__row--phone">
      <svg width="28" height="28" viewBox="0 0 24 24" aria-hidden="true"><path d="M6.6 10.8a15 15 0 0 0 6.6 6.6l2.2-2.2a1 1 0 0 1 1-.25 11.4 11.4 0 0 0 3.6.57 1 1 0 0 1 1 1V20a1 1 0 0 1-1 1A17 17 0 0 1 3 4a1 1 0 0 1 1-1h3.5a1 1 0 0 1 1 1c0 1.25.2 2.45.57 3.57a1 1 0 0 1-.25 1z" fill="none" stroke="var(--blue-deep)" stroke-width="2"/></svg>
      <span>0437 619 458</span>
    </div>
    <div class="contact__row contact__row--mail">
      <svg width="24" height="16" viewBox="0 0 26 18" aria-hidden="true"><rect x="1" y="1" width="24" height="16" fill="var(--blue-deep)"/><path d="M1,1 L13,10 L25,1" fill="none" stroke="var(--white)" stroke-width="2"/></svg>
      <span>admin@tulvenelectrics.example.au</span>
    </div>
    <div class="contact__row contact__row--social">
      <span class="contact__social-dot"></span>
      <span>TulvenElectrics</span>
    </div>
  </div>

  <div class="coupon">
    <span class="coupon__pct">10%</span>
    <span class="coupon__off">OFF</span>
    <span class="coupon__what">all electrical services</span>
    <span class="coupon__terms">*Terms conditions apply</span>
    <span class="coupon__expiry">Expires at <span class="coupon__expiry-field"></span></span>
  </div>

  <div class="footer-bar"></div>
</div>
</body>
</html>
```